New custom software business needs a Wordpress site

We need a Wordpress site for a new company based out of Chicago called 'Brackwell Consulting'. Using a mix of on and off-shore resources we build custom software solutions, mainly focusing on small to medium sized companies. We help our customers "aspire" to do great things.
We have a basic site up here: https://brackwellhq.com/. We worked on the content for it but not the branding. For now, this houses all the pages (except for a Contact Us page we'll be adding soon) for the foreseeable future.
We also have a new logo (attached) that we'd like to base the styling/colors on.
Target Market(s)
Small to medium sized companies that require tech resources
Industry/Entity Type
Software
Nice to have
- Teamwork, tech, professional but not elitist

```html
<!DOCTYPE html>
<html lang="en">
<head>
<meta charset="utf-8">
<title>Brackwell Consulting</title>
<link href="https://fonts.googleapis.com/css2?family=Orbitron:wght@500;600&family=Mulish:wght@400;600;700;800&display=swap" rel="stylesheet">
<style>
:root{
  --navy:#0b2651;
  --navy-deep:#081d40;
  --blue:#1f5db0;
  --blue-mid:#3b78c4;
  --blue-soft:#8fb2e6;
  --orange:#ff9a0a;
  --ink:#333b4a;
  --muted:#5a6272;
  --pale:#f1f5fc;
  --white:#ffffff;
}
*{box-sizing:border-box;margin:0;padding:0}
html,body{width:1200px;height:4695px;overflow:hidden}
body{font-family:"Mulish",sans-serif;color:var(--ink);background:var(--white);position:relative}
.abs{position:absolute}
section,header,footer{position:absolute;left:0;width:1200px}
.display{font-family:"Orbitron",sans-serif;font-weight:500;letter-spacing:2px;text-transform:uppercase}
.btn{position:absolute;display:flex;align-items:center;justify-content:center;background:var(--orange);color:var(--white);font-weight:800;font-size:15px;letter-spacing:.5px;text-transform:uppercase;clip-path:polygon(0 0,100% 0,86% 100%,0 100%);padding-right:16px}
.divider{position:absolute;left:500px;width:200px;height:20px}
.divider::before{content:"";position:absolute;left:0;right:0;top:10px;height:1px;background:var(--blue-mid)}
.divider::after{content:"";position:absolute;left:90px;top:0;width:20px;height:20px;border-radius:50%;background:var(--blue);box-shadow:0 0 0 4px var(--pale)}
.on-white .divider::after{box-shadow:0 0 0 4px var(--white)}
.section-title{position:absolute;left:0;width:1200px;text-align:center;color:var(--navy);font-size:40px}
.placeholder{position:absolute}

/* top bar */
.topbar{top:0;height:48px;background:var(--pale);font-size:15px;color:var(--blue)}
.topbar b{color:var(--navy);font-weight:700}
/* nav */
.nav{top:48px;height:116px;background:var(--white)}
.brand{position:absolute;display:flex;align-items:center;gap:10px;color:var(--blue);font-weight:800;font-size:24px;letter-spacing:1px}
.brand i{display:block;width:26px;height:26px;background:var(--blue)}
.nav-links{position:absolute;right:94px;top:44px;display:flex;gap:36px;font-size:15px;color:var(--navy);letter-spacing:.5px}

/* hero */
.hero{top:164px;height:588px;background:linear-gradient(90deg,#0a2148 0%,#0e2c59 60%,#143a6e 100%)}
.hero h1{position:absolute;left:91px;top:146px;color:var(--white);font-size:39px;line-height:53px;font-weight:600}
.hero h1 span{color:var(--blue-soft)}
.hero p{position:absolute;left:93px;top:316px;color:#cfd8e6;font-size:26px}

/* welcome */
.welcome{top:752px;height:457px}
.welcome p{position:absolute;left:264px;width:676px;top:192px;text-align:center;font-size:16.5px;line-height:27px;color:var(--ink)}

/* services */
.services{top:1209px;height:989px;background:var(--pale)}
.svc-title{position:absolute;color:var(--navy);font-size:22px;line-height:34px}
.svc-text{position:absolute;font-size:15px;line-height:25px;color:var(--muted)}

/* why */
.why{top:2198px;height:835px}
.why h3{position:absolute;width:300px;color:var(--navy);font-size:21px;line-height:31px}
.why p{position:absolute;width:290px;font-size:14.5px;line-height:22px;color:var(--muted)}
.why .left{text-align:right}

/* leadership */
.leaders{top:3033px;height:703px;background:var(--pale)}
.card{position:absolute;top:245px;width:493px;height:293px;background:var(--navy);border-radius:10px;box-shadow:0 0 24px rgba(40,90,180,.35)}
.card h4{position:absolute;left:200px;top:60px;color:var(--white);font-size:21px}
.card p{position:absolute;left:200px;top:108px;width:270px;color:#e3e9f3;font-size:15px;line-height:22px}
.card a{position:absolute;left:196px;top:218px;color:var(--white);font-size:15px;text-decoration:underline}

/* contact */
.contact{top:3736px;height:472px;background:linear-gradient(180deg,#1a3f72 0%,#133466 50%,#0f2c5b 100%)}
.contact .section-title{color:var(--white)}
.field{position:absolute;background:var(--white);font-size:15px;color:var(--ink);padding:10px 13px}

/* footer */
.footer{top:4208px;height:449px;background:var(--white)}
.footer h5{position:absolute;top:108px;font-family:"Orbitron",sans-serif;font-weight:500;font-size:16px;letter-spacing:1.5px;color:var(--navy);text-transform:uppercase}
.links{position:absolute;left:320px;top:157px;font-size:15px;line-height:35px;color:var(--navy)}
.qc{position:absolute;left:566px;top:156px;font-size:15px;line-height:22px;color:var(--navy)}
.qc .lbl{color:var(--blue)}
.vline{position:absolute;width:1px;background:#c9d3e4}
.mark{position:absolute;width:4px;height:30px;background:var(--blue)}
.social{position:absolute;top:4416px;width:40px;height:40px;border-radius:50%;background:var(--blue)}
.copy{top:4657px;height:38px;background:var(--navy-deep);color:var(--white);font-size:15px;display:flex;align-items:center;justify-content:center}
</style>
</head>
<body>

<header class="topbar">
  <div class="abs" style="left:91px;top:14px;display:flex;align-items:center;gap:8px">
    <svg width="20" height="14" viewBox="0 0 20 14"><rect x="1" y="1" width="18" height="12" rx="1" fill="var(--orange)"/><path d="M1 1l9 7 9-7" stroke="#fff" stroke-width="1.5" fill="none"/></svg>
    <span>Mail Us Now : <b>hello@brackwellhq.com</b></span>
  </div>
  <div class="abs" style="right:92px;top:14px;display:flex;align-items:center;gap:8px">
    <svg width="16" height="16" viewBox="0 0 16 16"><path d="M3 1l3 3-2 2c1 2 3 4 6 6l2-2 3 3-2 2C7 15 1 9 1 3z" fill="var(--orange)"/></svg>
    <span>Call Us Now : <b>312 555 0148</b></span>
  </div>
</header>

<header class="nav">
  <div class="brand" style="left:93px;top:44px"><i></i>BRACKWELL CONSULTING</div>
  <nav class="nav-links">
    <span>SERVICES</span><span>WHY BRACKWELL?</span><span>BRACKWELL LEADERSHIP</span><span>CONTACT US</span>
  </nav>
</header>

<section class="hero">
  <h1 class="display">We help our<br>customers <span>"aspire"</span><br>to do great things.</h1>
  <p>We Build Custom Software Solutions</p>
  <div class="btn" style="left:91px;top:383px;width:170px;height:46px">Contact Us</div>
  <div class="placeholder" role="img" aria-label="Illustration of a team climbing a large triangle toward an orange flag" style="left:565px;top:18px;width:548px;height:570px;background:linear-gradient(160deg,rgba(255,154,10,.25) 0%,rgba(60,120,196,.55) 45%,rgba(30,80,150,.35) 100%);clip-path:polygon(55% 0,100% 100%,0 100%)"></div>
</section>

<section class="welcome on-white">
  <h2 class="section-title display" style="top:78px">Welcome to Brackwell</h2>
  <div class="divider" style="top:141px"></div>
  <p>Welcome to Brackwell, a software consulting company specializing in serving small to medium size businesses. We understand the unique challenges and opportunities that these companies face, and we are dedicated to helping them succeed through innovative technology solutions.</p>
  <div class="btn" style="left:516px;top:320px;width:168px;height:45px">Read More</div>
</section>

<section class="services">
  <h2 class="section-title display" style="top:60px">Services</h2>
  <div class="divider" style="top:114px"></div>

  <h3 class="svc-title display" style="left:225px;width:300px;top:267px;text-align:right">Custom Solution<br>Delivery</h3>
  <p class="svc-text" style="left:165px;width:360px;top:336px;text-align:right">Brackwell offers a range of services focused on helping businesses and organizations deliver software solutions to their customers or users.</p>
  <div class="btn" style="left:356px;top:436px;width:169px;height:45px">Read More</div>
  <div class="placeholder" role="img" aria-label="Illustration of people working among large blue gears" style="left:666px;top:205px;width:406px;height:315px;background:radial-gradient(ellipse at 55% 55%,#5c7fe0 0%,#8fa9ee 45%,#c6d3f7 70%,rgba(198,211,247,0) 72%)"></div>

  <div class="placeholder" role="img" aria-label="Illustration of a team around a large blue light bulb" style="left:106px;top:633px;width:441px;height:265px;background:linear-gradient(180deg,rgba(200,213,247,0) 0%,#6d8fe6 35%,#3a66d6 70%,#c8d5f7 100%);border-radius:30px"></div>
  <h3 class="svc-title display" style="left:653px;top:680px">Staff Augmentation</h3>
  <p class="svc-text" style="left:653px;width:380px;top:717px">Let Brackwell help you supplement your existing software development teams with additional resources and expertise. We provided access to experienced.</p>
  <div class="btn" style="left:653px;top:843px;width:169px;height:46px">Read More</div>
</section>

<section class="why on-white">
  <h2 class="section-title display" style="top:78px">Why Brackwell?</h2>
  <div class="divider" style="top:147px"></div>

  <svg class="abs" style="left:0;top:0" width="1200" height="835" viewBox="0 0 1200 835">
    <defs>
      <linearGradient id="ringTop" x1="0" y1="0" x2="0" y2="1"><stop offset="0" stop-color="#4a86cc"/><stop offset="1" stop-color="#2f6bb9"/></linearGradient>
      <linearGradient id="ringBot" x1="0" y1="0" x2="0" y2="1"><stop offset="0" stop-color="#2a65b6"/><stop offset="1" stop-color="#1a4fa0"/></linearGradient>
    </defs>
    <g fill="none" stroke="var(--blue)" stroke-width="1.5">
      <path d="M531 264V300M531 264H235V300"/>
      <path d="M669 264V300M669 264H971V300"/>
      <path d="M531 740V692M531 740H235V702"/>
      <path d="M669 740V692M669 740H971V702"/>
    </g>
    <g fill="var(--blue)">
      <path d="M229 292l6 10 6-10z"/><path d="M965 292l6 10 6-10z"/>
      <path d="M229 710l6-10 6 10z"/><path d="M965 710l6-10 6 10z"/>
    </g>
    <g transform="translate(600 498)">
      <path d="M-8,-199 A199 199 0 0 0 -199,-8 L-133,-8 A133 133 0 0 1 -8,-133Z" fill="url(#ringTop)"/>
      <path d="M8,-199 A199 199 0 0 1 199,-8 L133,-8 A133 133 0 0 0 8,-133Z" fill="url(#ringTop)"/>
      <path d="M-199,8 A199 199 0 0 0 -8,199 L-8,133 A133 133 0 0 1 -133,8Z" fill="url(#ringBot)"/>
      <path d="M199,8 A199 199 0 0 1 8,199 L8,133 A133 133 0 0 0 133,8Z" fill="url(#ringBot)"/>
      <circle r="70" fill="#dbe6f6"/>
      <g fill="none" stroke="#fff" stroke-width="2">
        <circle cx="-107" cy="-131" r="8"/><circle cx="-125" cy="-124" r="6"/><circle cx="-89" cy="-124" r="6"/>
        <rect x="95" y="-143" width="24" height="28" rx="2"/><path d="M100-133h14M100-126h14"/>
        <circle cx="-132" cy="88" r="12"/><path d="M-140 108h18M-142 114h22"/>
        <circle cx="133" cy="102" r="16"/><path d="M125 102l6 6 10-12"/>
      </g>
    </g>
  </svg>

  <h3 class="display left" style="left:98px;top:311px">IT Professionals<br>Team</h3>
  <p class="left" style="left:106px;top:380px">At Brackwell, we are proud to have a team of seasoned IT professionals...</p>
  <h3 class="display" style="left:808px;top:311px">Delivering<br>Excellence</h3>
  <p style="left:808px;top:380px">Our team members are committed to delivering excellence in everything they do ...</p>
  <h3 class="display left" style="left:98px;top:551px">High-Quality<br>Software</h3>
  <p class="left" style="left:106px;top:620px">We understand that delivering a high-quality software solution requires.....</p>
  <h3 class="display" style="left:808px;top:551px">Develop a<br>Solution</h3>
  <p style="left:808px;top:620px">If you are in need of IT professionals who understand what it takes to deliver....</p>
</section>

<section class="leaders">
  <h2 class="section-title display" style="top:80px">Brackwell Leadership</h2>
  <div class="divider" style="top:153px;left:514px"></div>

  <article class="card" style="left:95px">
    <div class="placeholder" role="img" aria-label="Portrait photo of Dalton set in a triangle frame" style="left:24px;top:78px;width:155px;height:137px;background:linear-gradient(180deg,#9fb3cf 0%,#3b4f6e 100%);clip-path:polygon(50% 0,100% 100%,0 100%)"></div>
    <h4 class="display">Dalton</h4>
    <p>As a leader, Dalton is dedicated to fostering a culture of collaboration, innovation, and excellence within his team.</p>
    <a>Learn More</a>
  </article>
  <article class="card" style="left:609px">
    <div class="placeholder" role="img" aria-label="Portrait photo of Ravi set in a triangle frame" style="left:24px;top:78px;width:155px;height:137px;background:linear-gradient(180deg,#a7b7cc 0%,#44566f 100%);clip-path:polygon(50% 0,100% 100%,0 100%)"></div>
    <h4 class="display">Ravi</h4>
    <p>As a leader, Ravi is dedicated to fostering a culture of collaboration, innovation,and excellence within his team.</p>
    <a>Learn More</a>
  </article>

  <div class="btn" style="left:516px;top:580px;width:168px;height:44px">Contact Us</div>
</section>

<section class="contact" role="img" aria-label="Blue tinted photo of an office workspace behind the contact form">
  <h2 class="section-title display" style="top:102px">Contact Us</h2>
  <div class="field" style="left:348px;top:156px;width:248px;height:48px">Name</div>
  <div class="field" style="left:600px;top:156px;width:250px;height:48px">Email</div>
  <div class="field" style="left:348px;top:209px;width:502px;height:101px">Message</div>
  <div class="btn" style="left:516px;top:321px;width:165px;height:43px">Submit</div>
</section>

<footer class="footer">
  <div class="brand" style="left:97px;top:136px;font-size:19px;gap:8px"><i style="width:20px;height:20px"></i>BRACKWELL</div>
  <h5 style="left:319px">Quick Link</h5>
  <div class="links"><div>Services</div><div>Why Brackwell?</div><div>Brackwell Leadership</div><div>Contact Us</div></div>
  <div class="mark" style="left:507px;top:160px"></div>
  <div class="vline" style="left:510px;top:103px;height:264px"></div>

  <h5 style="left:565px">Quick Contact</h5>
  <div class="qc">
    <div class="lbl">Address:</div>
    <div>Harlow Building, Suite 410,</div>
    <div>Chicago, IL 60607</div>
    <div class="lbl" style="margin-top:22px">Email:</div>
    <div>hello@brackwellhq.com</div>
    <div class="lbl" style="margin-top:22px">Phone:</div>
    <div>312 555 0148</div>
  </div>
  <div class="mark" style="left:793px;top:160px"></div>
  <div class="vline" style="left:796px;top:103px;height:264px"></div>

  <h5 style="left:837px">Newsletter</h5>
  <div class="field" style="left:837px;top:157px;width:270px;height:53px;box-shadow:0 2px 10px rgba(20,50,110,.15);padding-top:17px">Enter Your Mail ID</div>
  <div class="btn" style="left:841px;top:217px;width:168px;height:44px">Subscribe</div>
</footer>
<div class="social" style="left:95px"></div>
<div class="social" style="left:140px"></div>
<div class="social" style="left:186px"></div>

<footer class="copy">© 2022 Brackwell. All Rights Reserved</footer>

</body>
</html>
```